Pinecrest Rapids Outfitters
In the Spirit of Fun and Adventure
Pinecrest Rapids Outfitters - Travel
Creative Brief
Bright & Fun-filled
Dale Hartwin
38217 Sorrel Ln Ridgefold Crossing, MT. 59412
www.paddlevortex.example
info@paddlevortex.example
38217 Sorrel Ln
Our logo is fairly clean and simple but would like to add a fun whitewater element to the card to liven it up.
Add A : Join the Adventure on: Friendspace Logo Journey Scout logo Clip Stream Logo Chirpline Logo

```html
<!DOCTYPE html>
<html lang="en">
<head>
<meta charset="utf-8">
<title>Pinecrest Rapids Outfitters Stationery</title>
<link rel="stylesheet" href="https://fonts.googleapis.com/css2?family=Open+Sans:wght@400;600;700&display=swap">
<style>
:root{
  --bg:#2b2d30;
  --paper:#ffffff;
  --navy:#0d3d7a;
  --blue:#1767b5;
  --sky:#2f8fd6;
  --ink:#1b3558;
  --grey:#7b8590;
  --label:#9aa1a8;
  --mist:#eef2f6;
}
*{margin:0;padding:0;box-sizing:border-box}
html,body{width:1200px;height:414px;overflow:hidden;background:var(--bg);font-family:"Open Sans",Arial,sans-serif}
.board{position:relative;width:1200px;height:414px}
.piece{position:absolute;background:var(--paper);box-shadow:0 3px 8px rgba(0,0,0,.5);overflow:hidden}
.brand{display:flex;align-items:center;gap:6px;font-weight:700;color:var(--navy);line-height:1.05;text-transform:uppercase;white-space:nowrap}
.brand .dot{border-radius:50%;background:currentColor;flex:none}
.brand-stack{flex-direction:column;gap:3px;text-align:center}
.label{position:absolute;font-size:7px;color:var(--label);text-align:center}
.hero{position:absolute;left:205px;top:62px;color:#fff;font-size:15px}
.hero .dot{width:34px;height:34px}
.small{font-size:5px;color:var(--grey);line-height:1.5;white-space:nowrap}
.name{font-size:7px;font-weight:700;color:var(--ink);white-space:nowrap}
/* vertical card */
.vcard{left:60px;top:91px;width:66px;height:150px}
.vcard .band{position:absolute;left:0;right:0;bottom:0;height:18px;background:var(--blue)}
.vcard .small{font-size:4.2px}
/* horizontal cards */
.hcard{top:156px;width:102px;height:84px}
.hcard .band{position:absolute;left:0;right:0;bottom:0;height:10px;background:var(--blue)}
.dark{background:var(--navy)}
.bright{background:var(--blue)}
.wave{position:absolute;left:0;bottom:0;width:100%;height:26px}
/* letterhead */
.letter{left:540px;top:91px;width:204px;height:293px}
.letter-contact{position:absolute;right:8px;top:14px;width:66px;font-size:4.6px}
.ghost{position:absolute;left:62px;top:120px;width:90px;height:90px;border-radius:50%;background:var(--mist)}
/* envelopes */
.env{width:250px;height:130px}
.flap{position:absolute;left:0;top:0;width:100%;height:60px}
</style>
</head>
<body>
<main class="board">
  <div class="brand hero"><span class="dot"></span><span>Pinecrest Rapids<br>Outfitters</span></div>

  <!-- vertical card -->
  <section class="piece vcard">
    <div class="name" style="position:absolute;left:6px;top:10px">Dale Hartwin</div>
    <div class="brand brand-stack" style="position:absolute;left:0;right:0;top:36px;font-size:5px"><span class="dot" style="width:12px;height:12px"></span><span>Pinecrest Rapids<br>Outfitters</span></div>
    <div class="small" style="position:absolute;left:5px;top:80px">38217 Sorrel Ln<br>(406) 555-0142<br>info@paddlevortex.example</div>
    <div class="band"></div>
  </section>
  <div class="label" style="left:55px;top:246px;width:76px">Vertical card</div>

  <section class="piece hcard" style="left:163px">
    <div class="brand" style="position:absolute;left:10px;top:16px;font-size:7px"><span class="dot" style="width:16px;height:16px"></span><span>Pinecrest Rapids<br>Outfitters</span></div>
    <div class="small" style="position:absolute;left:10px;top:44px">www.paddlevortex.example<br>38217 Sorrel Ln</div>
    <div class="band"></div>
  </section>
  <div class="label" style="left:163px;top:246px;width:102px">Card back</div>

  <section class="piece hcard" style="left:276px">
    <div class="name" style="position:absolute;left:8px;top:8px">Dale Hartwin</div>
    <div class="small" style="position:absolute;left:8px;top:22px">(406) 555-0142<br>info@paddlevortex.example<br>38217 Sorrel Ln Ridgefold<br>Crossing, MT. 59412</div>
    <div class="band"></div>
  </section>
  <div class="label" style="left:276px;top:246px;width:102px">Card front</div>

  <!-- bottom row -->
  <section class="piece hcard dark" style="left:60px;top:288px;height:72px;width:96px">
    <div class="brand" style="position:absolute;left:8px;top:12px;font-size:7px;color:#fff"><span class="dot" style="width:14px;height:14px"></span><span>Pinecrest Rapids<br>Outfitters</span></div>
    <div class="small" style="position:absolute;left:8px;top:44px;color:#cfe0f2">Join the Adventure on:<br>Friendspace · Journey Scout</div>
  </section>
  <div class="label" style="left:60px;top:364px;width:96px">Blue card front</div>

  <section class="piece hcard bright" style="left:163px;top:288px;height:72px">
    <div class="brand" style="position:absolute;left:10px;top:12px;font-size:7px;color:#fff"><span class="dot" style="width:14px;height:14px"></span><span>Pinecrest Rapids<br>Outfitters</span></div>
    <div class="small" style="position:absolute;left:10px;top:44px;color:#e3f0fb">Clip Stream · Chirpline<br>www.paddlevortex.example</div>
  </section>
  <div class="label" style="left:163px;top:364px;width:102px">Blue card back</div>

  <section class="piece hcard" style="left:276px;top:288px;height:72px">
    <div class="brand" style="position:absolute;left:14px;top:14px;font-size:7px"><span class="dot" style="width:14px;height:14px"></span><span>Pinecrest Rapids<br>Outfitters</span></div>
    <svg class="wave" viewBox="0 0 102 26" preserveAspectRatio="none"><path d="M0 14 Q26 2 51 14 T102 12 V26 H0Z" fill="#1767b5"/></svg>
  </section>
  <div class="label" style="left:276px;top:364px;width:102px">Light card</div>

  <!-- letterhead -->
  <section class="piece letter">
    <div class="brand" style="position:absolute;left:12px;top:14px;font-size:7px;gap:5px"><span class="dot" style="width:18px;height:18px"></span><span>Pinecrest Rapids<br>Outfitters</span></div>
    <div class="small letter-contact">38217 Sorrel Ln Ridgefold<br>Crossing, MT. 59412<br>(406) 555-0142<br>www.paddlevortex.example<br>info@paddlevortex.example</div>
    <div class="ghost"></div>
    <div style="position:absolute;left:0;right:0;bottom:0;height:4px;background:var(--blue)"></div>
  </section>
  <div class="label" style="left:540px;top:389px;width:204px">Letterhead</div>

  <!-- envelopes -->
  <section class="piece env" style="left:900px;top:80px">
    <svg class="flap" viewBox="0 0 250 60" preserveAspectRatio="none"><path d="M0 0H250L125 60Z" fill="#1767b5"/></svg>
  </section>
  <section class="piece env" style="left:870px;top:150px">
    <svg class="flap" viewBox="0 0 250 60" preserveAspectRatio="none"><path d="M0 0H250L125 60Z" fill="#eef2f6"/></svg>
  </section>
  <section class="piece env" style="left:830px;top:230px;width:270px">
    <svg class="flap" viewBox="0 0 270 60" preserveAspectRatio="none"><path d="M0 0H270V14Q135 60 0 30Z" fill="#0d3d7a"/></svg>
    <div class="brand" style="position:absolute;left:14px;top:38px;font-size:9px"><span class="dot" style="width:20px;height:20px"></span><span>Pinecrest Rapids<br>Outfitters</span></div>
    <div class="small" style="position:absolute;left:14px;top:70px">38217 Sorrel Ln Ridgefold Crossing, MT. 59412</div>
    <div style="position:absolute;right:30px;top:60px;width:60px;height:60px;border-radius:50%;background:var(--mist)"></div>
  </section>
  <div class="label" style="left:900px;top:389px;width:150px">Envelope</div>
</main>
</body>
</html>
```